Design für Wein-Etikett
Zielgruppe
Zielgruppe ist sowohl der traditionelle Weintrinker (der obendrein auf "Blaublütiges" steht), vor allem aber das junge, moderne Weinpublikum, welches die Message verstanden hat: "Traditionelles modern präsentiert".
Aufgabenstellung
Erstellung eines MODERNEN Weinflaschen-Etikettes, obwohl es auf der Tradition eines alten Prinzengeschlecht beruht. Das Etikett soll als Basis für eine künftige Weinlinie dienen, d.h. das Grundlayout bleibt bestehen, der Jahrgang, die Lagenbezeichnung, die Rebsorten und die AP-Nr. (Abfüllbetrieb) werden variieren.

```html
<!DOCTYPE html>
<html lang="de">
<head>
<meta charset="utf-8">
<title>Wendelheimer Sonnenberg – Weinetikett</title>
<link rel="stylesheet" href="https://fonts.googleapis.com/css2?family=Cinzel:wght@400;600&family=Cormorant+Garamond:wght@400;500;600&display=swap">
<style>
  :root {
    --page-bg: #ffffff;
    --label-blue: #1c3d9e;
    --label-blue-deep: #132b78;
    --label-cream: #f6f3ea;
    --ink-navy: #16265e;
    --ink-grey: #4a4a4a;
    --gold: #c9a64a;
    --gold-soft: #e2cf98;
    --white: #ffffff;
  }
  html, body {
    margin: 0;
    padding: 0;
    width: 1086px;
    height: 1200px;
    overflow: hidden;
    background: var(--page-bg);
  }
  .canvas {
    position: relative;
    width: 1086px;
    height: 1200px;
  }
  .wine-label {
    position: absolute;
    left: 283px;
    top: 50px;
    width: 520px;
    height: 1100px;
    background: var(--label-cream);
    box-shadow: 0 0 0 1px #e4dfd0;
    overflow: hidden;
    text-align: center;
  }
  .label-head {
    position: absolute;
    left: 0; top: 0;
    width: 100%; height: 286px;
    background: linear-gradient(180deg, var(--label-blue) 0%, var(--label-blue-deep) 100%);
    border-bottom: 3px solid var(--gold);
    box-shadow: 0 4px 0 0 var(--label-cream), 0 6px 0 0 var(--gold);
  }
  .head-ornament {
    position: absolute;
    left: 50%; top: 58px;
    transform: translateX(-50%);
  }
  .site-village {
    position: absolute;
    left: 0; top: 132px;
    width: 100%;
    margin: 0;
    font-family: "Cinzel", serif;
    font-weight: 400;
    font-size: 30px;
    letter-spacing: 4px;
    color: var(--white);
  }
  .site-name {
    position: absolute;
    left: 0; top: 170px;
    width: 100%;
    margin: 0;
    font-family: "Cinzel", serif;
    font-weight: 400;
    font-size: 56px;
    letter-spacing: 1px;
    color: var(--white);
  }
  .region {
    position: absolute;
    left: 0; top: 318px;
    width: 100%;
    font-family: "Cormorant Garamond", serif;
    font-size: 21px;
    letter-spacing: 3px;
    color: var(--ink-navy);
  }
  .vintage {
    position: absolute;
    left: 0; top: 340px;
    width: 100%;
    font-family: "Cormorant Garamond", serif;
    font-weight: 500;
    font-size: 72px;
    color: var(--ink-navy);
  }
  .crest-area {
    position: absolute;
    left: 140px; top: 440px;
  }
  .grape {
    position: absolute;
    left: 0; top: 650px;
    width: 100%;
    font-family: "Cinzel", serif;
    font-size: 26px;
    letter-spacing: 2px;
    color: var(--ink-navy);
  }
  .quality-line {
    position: absolute;
    left: 28px; right: 28px; top: 696px;
    display: flex;
    justify-content: space-between;
    align-items: baseline;
    font-family: "Cormorant Garamond", serif;
    color: var(--ink-grey);
  }
  .quality-line .volume { font-size: 15px; }
  .quality-line .quality { font-family: "Cinzel", serif; font-size: 14px; letter-spacing: 1.5px; color: var(--ink-navy); }
  .ap-number {
    position: absolute;
    left: 0; top: 724px;
    width: 100%;
    font-family: "Cormorant Garamond", serif;
    font-size: 12px;
    letter-spacing: 1px;
    color: var(--ink-grey);
  }
  .label-foot {
    position: absolute;
    left: 0; top: 770px;
    width: 100%; height: 330px;
    background: linear-gradient(180deg, var(--label-blue) 0%, var(--label-blue-deep) 100%);
    border-top: 3px solid var(--gold);
  }
  .edition {
    position: absolute;
    left: 0; top: 34px;
    width: 100%;
    font-family: "Cinzel", serif;
    font-size: 22px;
    letter-spacing: 3px;
    color: var(--white);
  }
  .house {
    position: absolute;
    left: 0; top: 74px;
    width: 100%;
    font-family: "Cinzel", serif;
    font-size: 17px;
    letter-spacing: 2px;
    color: var(--white);
  }
</style>
</head>
<body>
<main class="canvas">
  <article class="wine-label">
    <header class="label-head">
      <svg class="head-ornament" width="90" height="44" viewBox="0 0 90 44" role="img" aria-label="Kleines florales Ornament über dem Lagennamen">
        <ellipse cx="45" cy="22" rx="44" ry="20" fill="#8fa3dc" opacity="0.55"/>
      </svg>
      <h1 class="site-village">Wendelheimer</h1>
      <h2 class="site-name">Sonnenberg</h2>
    </header>

    <div class="region">MOSEL · SAAR · RUWER</div>
    <div class="vintage">2009</div>

    <svg class="crest-area" width="240" height="200" viewBox="0 0 240 200" role="img" aria-label="Blasses goldenes Fürstenwappen als Hintergrundmotiv">
      <defs>
        <radialGradient id="crestTone" cx="50%" cy="50%" r="55%">
          <stop offset="0%" stop-color="#e2cf98" stop-opacity="0.75"/>
          <stop offset="100%" stop-color="#e2cf98" stop-opacity="0.15"/>
        </radialGradient>
      </defs>
      <rect x="0" y="0" width="240" height="200" rx="24" fill="url(#crestTone)"/>
    </svg>

    <div class="grape">Riesling</div>
    <div class="quality-line">
      <span class="volume">12,5% vol</span>
      <span class="quality">Qualitätswein trocken</span>
      <span class="volume">0,75 l</span>
    </div>
    <div class="ap-number">A.P. Nr. 2418305 01710</div>

    <footer class="label-foot">
      <div class="edition">Edition</div>
      <div class="house">Prinz von Harlingen-Weilstein</div>
    </footer>
  </article>
</main>
</body>
</html>
```